Banner design

Hello.
I require a top header banner for my Interactive and electronic whiteboard / Audio Visual business.
Animated gif.

http://www.qorvantix.com.au

Basically a few photos, my phone number and my new logo (coming soon "Palquestron")
Corporate looking, that immediately captures the customers attention.

Target Market(s)

Adults in Western speaking country (Australia). To young business professionals, teachers, managers etc

Industry/Entity Type

Electronic

```html
<!DOCTYPE html>
<html lang="en">
<head>
<meta charset="utf-8">
<title>Qorvantix — Audio Visual</title>
<link href="https://fonts.googleapis.com/css2?family=Arimo:wght@400;700&display=swap" rel="stylesheet">
<style>
:root{
  --green:#3fc22c;
  --green-dark:#2a9a1c;
  --green-light:#8ee07a;
  --ink:#1f1f1f;
  --grey-text:#333;
  --rule:#c9c9c9;
  --pill-top:#f4f4f4;
  --pill-bottom:#bdbdbd;
  --logo:#2c2c2c;
}
*{box-sizing:border-box;margin:0;padding:0}
html,body{width:1200px;height:1000px;overflow:hidden;background:#fff;font-family:"Arimo",Arial,sans-serif;color:var(--ink)}
.page{position:relative;width:1200px;height:1000px}

/* header */
.masthead{position:absolute;left:0;top:0;width:1200px;height:400px;background:linear-gradient(180deg,#fff 0,#fff 120px,#eef1f3 260px,#fff 400px)}
.brand{position:absolute;left:176px;top:4px;width:840px;height:116px;display:flex;align-items:center;gap:18px}
.brand-mark{width:42px;height:42px;border-radius:50%;background:var(--green)}
.brand-name{font-size:78px;font-weight:700;color:var(--logo);letter-spacing:1px}
.office-photo{position:absolute;left:430px;top:128px;width:770px;height:240px;background:linear-gradient(100deg,#d6dde2 0,#aab6be 40%,#5a6770 75%,#c7cfd4 100%);clip-path:polygon(8% 0,100% 0,100% 100%,0 100%)}
.product{position:absolute;border:5px solid #111;border-radius:10px;background:#fff}
.product-board{left:0;top:268px;width:200px;height:130px;transform:rotate(-4deg);background:linear-gradient(180deg,#f5f5f5,#d9dde0)}
.product-projector{left:200px;top:276px;width:196px;height:118px;background:linear-gradient(180deg,#f2f2f2,#cfcfcf)}
.product-speakers{left:398px;top:256px;width:196px;height:134px;transform:rotate(4deg);background:linear-gradient(180deg,#6a6a6a,#1d1d1d)}
.phone-line{position:absolute;right:14px;top:362px;font-size:19px;letter-spacing:2px;color:#111}

/* navigation */
.nav{position:absolute;display:flex;align-items:center;white-space:nowrap;background:linear-gradient(180deg,var(--green-light),var(--green) 45%,var(--green-dark));}
.nav-main{left:0;top:400px;width:1200px;height:36px;justify-content:flex-end;padding-right:18px;border-bottom:4px solid #111}
.nav-sub{left:180px;top:446px;width:1020px;height:38px;justify-content:flex-start;padding-left:2px}
.nav a{color:#111;text-decoration:none;font-size:21px;padding:0 8px;border-left:2px solid #111;line-height:24px;white-space:nowrap;flex:none}
.nav-sub a{color:#fff;border-left-color:#fff;font-size:20px;padding:0 6px}
.nav a:first-child{border-left:none}

/* sidebar */
.sidebar{position:absolute;left:0;top:500px;width:232px}
.panel-head{height:48px;border-radius:14px;background:linear-gradient(180deg,var(--pill-top),var(--pill-bottom));border:2px solid #9a9a9a;display:flex;align-items:center;padding:0 16px;position:relative}
.panel-head::before{content:"";width:22px;height:22px;border-radius:50%;background:radial-gradient(circle at 35% 35%,#b7f0a5,var(--green) 60%,var(--green-dark));margin-right:auto}
.panel-head span{font-weight:700;font-size:20px;color:#222;margin-right:4px;white-space:nowrap}
.category-list{list-style:none;padding:30px 0 0 10px}
.category-list li{position:relative;padding-left:24px;font-size:22px;line-height:34px;color:#111}
.category-list li::before{content:"";position:absolute;left:0;top:10px;width:13px;height:13px;border-radius:50%;background:var(--green)}
.info-head{margin-top:18px}

/* content */
.content{position:absolute;left:240px;top:494px;width:760px}
.breadcrumb{font-weight:700;font-size:22px;color:#333;padding-bottom:10px;border-bottom:1px solid var(--rule)}
.content p{font-size:22px;line-height:34px;color:var(--grey-text);margin-top:30px}
.service-list{list-style:none;margin-top:36px}
.service-list li{font-weight:700;font-size:22px;line-height:30.5px;color:#333}

/* right column */
.aside{position:absolute;left:1018px;top:500px;width:200px}
.aside .panel-head{border-radius:14px 0 0 14px;border-right:none;width:200px}
.aside p{font-size:22px;line-height:30px;color:#111}
.basket-note{margin:18px 0 20px 12px;white-space:nowrap}
.member-note{margin:20px 0 22px 0;text-align:center;white-space:nowrap}
.search-box{display:flex;margin-top:18px;gap:4px}
.search-box span{border:2px solid #999;padding:2px 6px;font-size:22px;width:146px}
.search-box b{background:#ccc;width:40px}
.advanced{margin-top:8px;text-align:center;white-space:nowrap;color:#333;font-size:22px}
.last-head{margin-top:12px}
</style>
</head>
<body>
<div class="page">
  <header class="masthead">
    <div class="brand"><span class="brand-mark"></span><span class="brand-name">Qorvantix.com.au</span></div>
    <div class="office-photo" role="img" aria-label="Photo of business people meeting in a glass-walled boardroom"></div>
    <div class="product product-board" role="img" aria-label="Photo of an interactive whiteboard on a stand"></div>
    <div class="product product-projector" role="img" aria-label="Photo of a data projector and remote"></div>
    <div class="product product-speakers" role="img" aria-label="Photo of a pair of audio speakers"></div>
    <div class="phone-line">Phone: 0400 555 019 or (02) 5550 4827</div>
  </header>

  <nav class="nav nav-main">
    <a href="#">Hire</a><a href="#">Electronic Whiteboards</a><a href="#">Interactive Whiteboards</a><a href="#">Repairs &amp; Service</a><a href="#">Accessories</a><a href="#">Audio Visual</a><a href="#">Projector Lamps</a>
  </nav>
  <nav class="nav nav-sub">
    <a href="#">Home</a><a href="#">Contact Us</a><a href="#">Testimonials</a><a href="#">Trade-In</a><a href="#">Employment</a><a href="#">Order Tracking</a><a href="#">View Cart / Basket</a>
  </nav>

  <aside class="sidebar">
    <div class="panel-head"><span>Categories</span></div>
    <ul class="category-list">
      <li>HIRE</li>
      <li>Electronic Whiteboards</li>
      <li>Interactive Whiteboards</li>
      <li>Repairs &amp; Service</li>
      <li>Accessories</li>
      <li>Audio Visual</li>
      <li>Trade-In</li>
      <li>Projector Lamps</li>
    </ul>
    <div class="panel-head info-head"><span>Information</span></div>
  </aside>

  <main class="content">
    <div class="breadcrumb">Home » Audio Visual</div>
    <p>What do you do if you need Audio Visual Equipment? Contact us at Qorvantix of course!</p>
    <p>We can provide you with the very best prices on all Audio Visual Equipment that you'll find anywhere.</p>
    <ul class="service-list">
      <li>Interactive Whiteboards</li>
      <li>Electronic Whiteboards</li>
      <li>Video Data Projectors</li>
      <li>Projection Screens</li>
      <li>Projector Lamps</li>
      <li>Audio Speakers</li>
      <li>Microphones</li>
      <li>&amp; More</li>
    </ul>
  </main>

  <aside class="aside">
    <div class="panel-head"><span>Shopping C</span></div>
    <p class="basket-note">Your basket is emp</p>
    <div class="panel-head"><span>Memb</span></div>
    <p class="member-note">Please click <b>here</b><br>sign in or registe</p>
    <div class="panel-head"><span>Sea</span></div>
    <div class="search-box"><span>Keywords...</span><b></b></div>
    <div class="advanced">Advanced Searc</div>
    <div class="panel-head last-head"><span></span></div>
  </aside>
</div>
</body>
</html>
```